Crest of Morning Paddocks Business Cards with logo

Need a creative business card that pops. Colorful but professional. The attached logo should be included. We are a national horse racing partnership so we are in the equine business. Nothing cartoonlike or whimsical.

Target Market(s)

professionals - 40+

Contact Information for Business Card

Maren Dunleavy
Director of Operations
27 Ashbrook Lane
Middletown, MD. 21584

Phone (313) 555-0147

FX: (949) 555-0192

email: maren@cmpaddocks.example
cmpaddocks.example

Requirements
Must have
• All information above should be on the business card including the website address. Professional yet creative
Nice to have
• an attention grabbing design. not boring. exciting.
Should not have
• cartoon like - whimsical.

```html
<!DOCTYPE html>
<html lang="en">
<head>
<meta charset="utf-8">
<title>Crest of Morning Paddocks — Business Cards</title>
<link href="https://fonts.googleapis.com/css2?family=Montserrat:wght@400;500;700&display=swap" rel="stylesheet">
<style>
  :root {
    --navy: #1f2a6b;
    --gold: #b08a2e;
    --ink: #1c1c1c;
    --card: #f4f4f5;
    --card-edge: #e4e4e6;
    --backdrop: #8d8f93;
    --fade-cream: rgba(232, 214, 160, .38);
    --fade-lilac: rgba(170, 176, 214, .38);
  }
  * { box-sizing: border-box; margin: 0; padding: 0; }
  html, body { width: 1200px; height: 1021px; overflow: hidden; }
  body {
    background: var(--backdrop);
    font-family: "Montserrat", sans-serif;
    color: var(--ink);
    position: relative;
  }
  .card {
    position: absolute;
    left: 250px;
    width: 700px;
    height: 400px;
    overflow: hidden;
    background: linear-gradient(135deg, #ffffff 0%, var(--card) 60%, var(--card-edge) 100%);
    box-shadow: 0 10px 28px rgba(0,0,0,.35);
  }
  .card--front { top: 70px; }
  .card--back { top: 550px; }

  .brand {
    display: flex;
    flex-direction: column;
    align-items: center;
    text-align: center;
    z-index: 2;
  }
  .brand__ring {
    width: 150px; height: 150px;
    border: 2px solid var(--gold);
    border-radius: 50%;
    display: flex; align-items: center; justify-content: center;
    padding: 18px;
  }
  .brand__name {
    color: var(--navy);
    font-weight: 700;
    font-size: 17px;
    line-height: 1.25;
    letter-spacing: .06em;
    text-transform: uppercase;
  }
  .card--front .brand {
    position: absolute; left: 50%; top: 50%;
    transform: translate(-50%, -50%);
  }
  .card--front .brand__ring { width: 190px; height: 190px; }
  .card--front .brand__name { font-size: 20px; }

  .card__backdrop {
    position: absolute;
    left: 330px; top: 60px;
    width: 350px; height: 360px;
    border-radius: 14px 14px 0 0;
    background:
      radial-gradient(circle at 52% 40%, var(--fade-lilac) 0 26%, transparent 27%),
      linear-gradient(160deg, var(--fade-cream) 0%, var(--fade-cream) 55%, var(--fade-lilac) 100%);
    z-index: 1;
  }

  .card--back .brand { position: absolute; left: 60px; top: 40px; }
  .address {
    position: absolute; left: 60px; top: 230px;
    font-size: 17px; line-height: 1.35;
    z-index: 2;
  }
  .person {
    position: absolute; right: 60px; top: 100px;
    text-align: right;
    z-index: 2;
  }
  .person__name { color: var(--navy); font-weight: 700; font-size: 24px; }
  .person__title { font-size: 17px; margin-top: 2px; }
  .contacts {
    position: absolute; right: 60px; bottom: 45px;
    list-style: none; text-align: right;
    font-size: 18px; line-height: 1.5;
    z-index: 2;
  }
  .contacts li { display: flex; align-items: center; justify-content: flex-end; gap: 10px; }
  .contacts svg { width: 18px; height: 18px; fill: none; stroke: var(--gold); stroke-width: 2; }
</style>
</head>
<body>
  <section class="card card--front">
    <div class="brand">
      <div class="brand__ring"><span class="brand__name">Crest of Morning Paddocks</span></div>
    </div>
  </section>

  <section class="card card--back">
    <div class="card__backdrop" role="img" aria-label="Large faded racing silks illustration in soft cream and lilac"></div>

    <div class="brand">
      <div class="brand__ring"><span class="brand__name">Crest of Morning Paddocks</span></div>
    </div>
    <p class="address">27 Ashbrook Lane<br>Middletown, MD. 21584</p>

    <div class="person">
      <p class="person__name">Maren Dunleavy</p>
      <p class="person__title">Director of Operations</p>
    </div>

    <ul class="contacts">
      <li>(313) 555-0147
        <svg viewBox="0 0 24 24" aria-label="Phone"><path d="M6 3l3 4-2 2a12 12 0 0 0 8 8l2-2 4 3-2 3C10 21 3 14 3 5z"/></svg></li>
      <li>(949) 555-0192
        <svg viewBox="0 0 24 24" aria-label="Fax"><rect x="6" y="3" width="12" height="6"/><rect x="3" y="9" width="18" height="9"/><rect x="7" y="15" width="10" height="6"/></svg></li>
      <li>maren@cmpaddocks.example
        <svg viewBox="0 0 24 24" aria-label="Email"><rect x="3" y="6" width="18" height="12"/><path d="M3 6l9 7 9-7"/></svg></li>
      <li>cmpaddocks.example
        <svg viewBox="0 0 24 24" aria-label="Website"><circle cx="12" cy="12" r="9"/><path d="M3 12h18M12 3c4 4 4 14 0 18M12 3c-4 4-4 14 0 18"/></svg></li>
    </ul>
  </section>
</body>
</html>
```